Business card-Beneath The Copper Kite

Looking for a business card. I have a website I designed "BeneathTheCopperKite.example I am not a graphic artist and may at some point need help with my website too. Used the font "Hello Stockholm" on my website. I am a writer, looking to get published. Liked the "feel" of the cover below. No cliche typwriters, keyboards, pens. - Marcus T. Delaney
Updates

Not 100% sold on needing the owls, just a place to begin. I probably sounds like I'm going to be a pain to work with, I was a video production manager for 15+ years. When I would give an editor or graphic artist a project and let them run with it, the results were typically beyond my expectations. I give the idea then as the artists touch it, and adds value I could never bring to the project. Make something you would be proud of, don't try to second-guess me.

Target Market(s)

Agents, publishers, people I want to buy my book once I get it published

Industry/Entity Type

Publishing

Contact Information for Business Card

Marcus T. Delaney
BeneathTheCopperKite.example
Phone #-TBD
Marcus@BeneathTheCopperKtie.example
Maybe address; 418 E. 7th St Cheyenne, WY 82614

Colors
fcca95
3277b5

Requirements
Must have
• I like the "chromatic" feel of the attached cover. As you can see from my website, I'm an owl fan. Those pictures I took and do own the rights too. Not sure if they are approritae for a business card.
Should not have
• Cliche I like the "chromatic" feel of the attached book cover.
• I will need help with my website at some point too. I want the website to be easy for me to update, and reflect the same feel as the card. I write adventure, mystery. I have romance in my books too...Adventure of Romance, Romance of adventure, I am not sure but those words were like by an author firned of mine. They are rather "light" reading too.

```html
<!DOCTYPE html>
<html lang="en">
<head>
<meta charset="UTF-8">
<title>Marcus T. Delaney — Business Card</title>
<link rel="stylesheet" href="https://fonts.googleapis.com/css2?family=Oswald:wght@400&family=Roboto:wght@300&display=swap">
<style>
  :root {
    --page-bg: #4a433c;
    --card-shade: #3b3430;
    --photo-warm: #6b5a4c;
    --photo-deep: #2e2823;
    --photo-shirt: #4a3026;
    --photo-wall: #8a7c70;
    --accent-blue: #3277b5;
    --text-light: #f2efeb;
    --rule: rgba(255, 255, 255, 0.85);
  }
  * { margin: 0; padding: 0; box-sizing: border-box; }
  html, body {
    width: 1200px;
    height: 930px;
    overflow: hidden;
    background: var(--page-bg);
  }
  .card {
    position: absolute;
    left: 100px;
    top: 179px;
    width: 1000px;
    height: 572px;
    border-radius: 22px;
    overflow: hidden;
    background: var(--card-shade);
    box-shadow: 0 10px 30px rgba(0, 0, 0, 0.35);
  }
  .card-photo {
    position: absolute;
    inset: 0;
    background:
      radial-gradient(ellipse 18% 48% at 40% 62%, var(--photo-deep) 0%, rgba(46,40,35,0.6) 60%, transparent 100%),
      radial-gradient(ellipse 30% 55% at 82% 30%, var(--photo-shirt) 0%, rgba(74,48,38,0.5) 55%, transparent 100%),
      linear-gradient(100deg, var(--photo-wall) 0%, var(--photo-warm) 35%, var(--photo-deep) 70%, var(--photo-shirt) 100%);
  }
  .card-dim {
    position: absolute;
    inset: 0;
    background: rgba(30, 25, 22, 0.45);
  }
  .identity {
    position: absolute;
    left: 200px;
    top: 330px;
  }
  .identity-name {
    font-family: "Oswald", sans-serif;
    font-weight: 400;
    font-size: 46px;
    letter-spacing: 1px;
    line-height: 1;
    color: var(--accent-blue);
    text-transform: uppercase;
  }
  .identity-role {
    margin-top: 6px;
    font-family: "Roboto", sans-serif;
    font-weight: 300;
    font-size: 20px;
    color: var(--text-light);
  }
  .divider {
    position: absolute;
    left: 228px;
    top: 424px;
    width: 690px;
    height: 2px;
    background: var(--rule);
  }
  .contact {
    position: absolute;
    left: 228px;
    top: 442px;
    font-family: "Roboto", sans-serif;
    font-weight: 300;
    font-size: 19px;
    line-height: 32px;
    color: var(--text-light);
    list-style: none;
    white-space: nowrap;
  }
</style>
</head>
<body>
  <article class="card">
    <div class="card-photo" role="img" aria-label="Photograph of a great horned owl perched beside a person in a brown shirt"></div>
    <div class="card-dim"></div>
    <header class="identity">
      <h1 class="identity-name">Marcus T. Delaney</h1>
      <p class="identity-role">Director</p>
    </header>
    <div class="divider"></div>
    <ul class="contact">
      <li>P : +307 555-0148 | E : Marcus@BeneathTheCopperKtie.example</li>
      <li>W : www.BeneathTheCopperKite.example | A : 418 E. 7th St Cheyenne, WY 82614</li>
    </ul>
  </article>
</body>
</html>
```